Car finance company business card

Create a nice business card for our car financing company , Visit our website www.birchlanefinance.com for the phone number and idea of the company look. Please do not be afraid to be creative. Name on card Is Marc-Antoine Beaulieu and phone number is on our website adress of business is
27816 Boulevard Saint-Orvel,
Val-Ombreuse, ON K4R 2T8

```html
<!DOCTYPE html>
<html lang="en">
<head>
<meta charset="utf-8">
<title>Birch Lane Finance — Business Card</title>
<link href="https://fonts.googleapis.com/css2?family=Roboto:wght@400;500;700&family=Roboto+Condensed:wght@700&display=swap" rel="stylesheet">
<style>
  :root {
    --page-bg: #e9e9e9;
    --card-white: #ffffff;
    --brand-blue: #1380c6;
    --name-blue: #1a7cc4;
    --text-grey: #555555;
    --divider: #c9c9c9;
    --brand-dark: #1b1b1b;
    --brand-accent: #e8742a;
  }
  html, body {
    margin: 0;
    padding: 0;
    width: 1125px;
    height: 1200px;
    overflow: hidden;
    background: var(--page-bg);
    font-family: "Roboto", Arial, sans-serif;
  }
  .canvas {
    position: relative;
    width: 1125px;
    height: 1200px;
  }
  .card {
    position: absolute;
    left: 171px;
    width: 826px;
    height: 472px;
    box-sizing: border-box;
  }
  .card--front { top: 106px; background: var(--card-white); }
  .card--back  { top: 640px; background: var(--brand-blue); }

  .brand-mark {
    position: absolute;
    display: flex;
    align-items: center;
    gap: 16px;
  }
  .brand-mark__dot {
    flex: none;
    border-radius: 50%;
    background: var(--brand-accent);
  }
  .brand-mark__name {
    font-family: "Roboto", Arial, sans-serif;
    font-weight: 700;
    color: var(--brand-dark);
    line-height: 1.05;
  }
  .card--front .brand-mark { left: 60px; top: 193px; }
  .card--front .brand-mark__dot { width: 74px; height: 74px; }
  .card--front .brand-mark__name { font-size: 40px; }

  .card--back .brand-mark { left: 226px; top: 160px; }
  .card--back .brand-mark__dot { width: 104px; height: 104px; background: var(--card-white); }
  .card--back .brand-mark__name { font-size: 56px; color: var(--card-white); }

  .divider {
    position: absolute;
    left: 446px;
    top: 136px;
    width: 1px;
    height: 196px;
    background: var(--divider);
  }
  .contact {
    position: absolute;
    left: 481px;
    top: 153px;
    color: var(--text-grey);
  }
  .contact__name {
    margin: 0 0 14px;
    font-family: "Roboto Condensed", "Arial Narrow", sans-serif;
    font-weight: 700;
    font-size: 30px;
    color: var(--name-blue);
    letter-spacing: 0.2px;
  }
  .contact__address {
    margin: 0 0 16px;
    font-size: 19px;
    line-height: 25px;
    font-style: normal;
  }
  .contact__line {
    display: flex;
    align-items: center;
    gap: 9px;
    font-size: 19px;
    line-height: 26px;
  }
  .contact__icon { width: 17px; height: 17px; flex: none; }

  .back-url {
    position: absolute;
    left: 0;
    right: 0;
    top: 378px;
    margin: 0;
    text-align: center;
    color: var(--card-white);
    font-size: 19px;
    letter-spacing: 7.5px;
  }
</style>
</head>
<body>
<main class="canvas">
  <section class="card card--front" aria-label="Business card front">
    <div class="brand-mark">
      <span class="brand-mark__dot"></span>
      <span class="brand-mark__name">Birch Lane<br>Finance</span>
    </div>
    <div class="divider"></div>
    <div class="contact">
      <h1 class="contact__name">Marc-Antoine Beaulieu</h1>
      <address class="contact__address">27816 Boulevard Saint-Orvel<br>Val-Ombreuse, ON K4R 2T8</address>
      <div class="contact__line">
        <svg class="contact__icon" viewBox="0 0 24 24" aria-hidden="true"><path fill="#1a7cc4" d="M6.6 10.8a15.1 15.1 0 0 0 6.6 6.6l2.2-2.2c.3-.3.7-.4 1-.2 1.1.4 2.3.6 3.6.6.6 0 1 .4 1 1V20c0 .6-.4 1-1 1A17 17 0 0 1 3 4c0-.6.4-1 1-1h3.5c.6 0 1 .4 1 1 0 1.3.2 2.5.6 3.6.1.3 0 .7-.2 1z"/></svg>
        <span>(450) 555-0187</span>
      </div>
      <div class="contact__line">
        <svg class="contact__icon" viewBox="0 0 24 24" aria-hidden="true"><circle cx="12" cy="12" r="10" fill="#1a7cc4"/><path fill="#fff" d="M7 7c2 0 3 1 3 2.5S8 11 9 13s3 1 3 3-1 3-1 4c-3-.5-6-3-6.5-6S5 8 7 7zm7-2c2 .5 4 2 5 4-1.5 0-2.5 1-2 2.5s2 1 2.5 2.5c-.5 2-2 3.5-3 4 .5-2-1-3-1-4.5S16 10 14.5 9 13 6 14 5z"/></svg>
        <span>www.birchlanefinance.com</span>
      </div>
    </div>
  </section>

  <section class="card card--back" aria-label="Business card back">
    <div class="brand-mark">
      <span class="brand-mark__dot"></span>
      <span class="brand-mark__name">Birch Lane<br>Finance</span>
    </div>
    <p class="back-url">www.birchlanefinance.com</p>
  </section>
</main>
</body>
</html>
```